I need a business card for myself, being a proprietor of a funeral parlor based in Manila. I'd like the card to have either of the following:
White Font on Black Background
or
Black Font on White Background
No logo is needed however I will appreciate any efforts to show a symbol of eternal happiness, aptly designed with above mentioned colors in mind.
Company name, address and contact on the lower right corner.
Logo or symbol anywhere.
Quillstone Funeral Services
+639174826351
darvik4521@pelmora.com
corner of Brisco Avenue and Velhurst Street
Makati City, Philippines
Thank you.
Update: Please include a small dove in your design. You are free to choose where you would like it on the card.

```html
<!DOCTYPE html>
<html lang="en">
<head>
<meta charset="utf-8">
<title>Quillstone Funeral Services – Business Card</title>
<link rel="stylesheet" href="https://fonts.googleapis.com/css2?family=Play&display=swap">
<style>
  :root {
    --backdrop: #000000;
    --card: #ffffff;
    --ink: #111111;
    --symbol-fill: #d9d9d9;
  }
  html, body {
    margin: 0;
    padding: 0;
    width: 1200px;
    height: 1000px;
    overflow: hidden;
    background: var(--backdrop);
  }
  .canvas {
    position: relative;
    width: 1200px;
    height: 1000px;
    background: var(--backdrop);
  }
  .business-card {
    position: absolute;
    left: 75px;
    top: 200px;
    width: 1050px;
    height: 600px;
    background: var(--card);
    font-family: "Play", sans-serif;
    color: var(--ink);
  }
  .eternal-symbol {
    position: absolute;
    left: 92px;
    top: 37px;
    width: 416px;
    height: 536px;
  }
  .company-name {
    position: absolute;
    right: 82px;
    top: 22px;
    margin: 0;
    font-weight: 400;
    font-size: 66px;
    line-height: 92px;
    text-align: right;
    letter-spacing: 0.5px;
  }
  .company-name span { display: block; }
  .contact-details {
    position: absolute;
    right: 82px;
    top: 323px;
    margin: 0;
    font-style: normal;
    font-size: 29px;
    text-align: right;
    line-height: 44px;
    letter-spacing: 0.3px;
  }
  .contact-details .phone,
  .contact-details .email { display: block; margin-bottom: 14px; }
  .contact-details .address-line { display: block; }
</style>
</head>
<body>
<div class="canvas">
  <section class="business-card">
    <svg class="eternal-symbol" viewBox="0 0 416 536" role="img" aria-label="Endless knot symbol of eternal happiness in black line work">
      <polygon points="208,0 416,268 208,536 0,268" fill="var(--symbol-fill)"/>
    </svg>
    <h1 class="company-name">
      <span>Quillstone</span>
      <span>Funeral</span>
      <span>Services</span>
    </h1>
    <address class="contact-details">
      <span class="phone">+639174826351</span>
      <span class="email">darvik4521@pelmora.com</span>
      <span class="address-line">Corner of Brisco Avenue</span>
      <span class="address-line">and Velhurst Street</span>
      <span class="address-line">Makati City, Philippines</span>
    </address>
  </section>
</div>
</body>
</html>
```